Printed Promo Flyer for new pet business

We need a double sided flyer design as per the given example flyer, just better looking and more fun.Flyers will need to be printed.Flyer size approx 10.5cm x 15cm. The text will need to be amended slightly afterwards to be more fun unless you can create a new tone of voice as well (should sound fun like breezy do it) Look and Feel: emotional, fun, loving, professional
See attached files.

Target Market(s)

Pet owners in the UK who want the convenience of getting their pets parasite treatment delivered to their door without the need of having to run to the vet or store for purchase

Industry/Entity Type

Pet Care

Colors
00a990
6b449b

Requirements
Must have
• all the content context as given in the example flyer.
Nice to have
• Tone of voice can be changed to be more fun (using Breezy as a guide)

```html
<!DOCTYPE html>
<html lang="en">
<head>
<meta charset="utf-8">
<title>Paw Post – Promo Flyer</title>
<link href="https://fonts.googleapis.com/css2?family=Roboto+Condensed:ital,wght@0,400;0,700;0,800;1,700;1,800&family=Source+Sans+3:wght@400;600;700&display=swap" rel="stylesheet">
<style>
  :root {
    --teal: #00a990;
    --teal-soft: #4fb8b0;
    --teal-deep: #14978e;
    --purple: #6b449b;
    --purple-deep: #4e1a78;
    --purple-panel: #8e45c4;
    --white: #ffffff;
    --ink: #222222;
    --yellow: #f7ec1c;
    --stage: #5c5c5c;
  }
  * { box-sizing: border-box; margin: 0; padding: 0; }
  html, body { width: 1200px; height: 1200px; overflow: hidden; }
  body { background: var(--stage); position: relative; font-family: "Source Sans 3", sans-serif; }

  .flyer {
    position: absolute; left: 200px; top: 30px;
    width: 800px; height: 1140px;
    background: var(--white); overflow: hidden;
  }

  .pet-photo {
    position: absolute; left: 0; top: 114px; width: 402px; height: 424px;
    background: linear-gradient(160deg, #f3ead9 0%, #e7d2a8 45%, #c98a4a 100%);
  }

  .brand { position: absolute; left: 500px; top: 118px; width: 270px; text-align: center; }
  .brand-mark { display: inline-block; width: 26px; height: 26px; border-radius: 50%; background: var(--teal); margin-bottom: 10px; }
  .brand-name {
    font-family: "Roboto Condensed", sans-serif; font-weight: 700;
    font-size: 52px; letter-spacing: 2px; color: var(--purple); line-height: 1;
  }

  .bubble { position: absolute; left: 370px; top: 218px; width: 430px; height: 316px; }
  .bubble-text {
    position: absolute; left: 430px; top: 240px; width: 342px; text-align: right;
    font-family: "Roboto Condensed", sans-serif; font-style: italic; color: var(--white);
    white-space: nowrap;
  }
  .bubble-text .lead { font-weight: 800; font-size: 46px; line-height: 1; padding-right: 4px; }
  .bubble-text .line { font-weight: 700; font-size: 41px; line-height: 1.06; padding-right: 8px; }
  .bubble-text .sign { font-weight: 700; font-size: 24px; margin-top: 10px; padding-right: 60px; }

  .lower {
    position: absolute; left: 0; top: 538px; width: 800px; height: 584px;
    background: linear-gradient(90deg, var(--purple-deep) 0%, var(--purple) 55%, var(--purple-deep) 100%);
  }
  .base-strip { position: absolute; left: 0; top: 1122px; width: 800px; height: 18px; background: var(--teal-deep); }

  .why-shape { position: absolute; left: 0; top: 538px; width: 800px; height: 584px; }

  .why-title {
    position: absolute; left: 28px; top: 552px;
    font-family: "Roboto Condensed", sans-serif; font-weight: 800;
    font-size: 36px; line-height: 0.95; color: var(--teal);
  }

  .benefits { position: absolute; left: 28px; top: 692px; width: 240px; }
  .benefit { margin-bottom: 12px; }
  .benefit h3 { font-weight: 700; font-size: 20px; color: var(--teal); line-height: 1.1; }
  .benefit p { font-size: 15px; color: var(--ink); line-height: 1.3; }

  .icon-bubble {
    position: absolute; width: 140px; height: 118px; border-radius: 50%;
    background: var(--white); display: flex; align-items: center; justify-content: center;
  }
  .icon-bubble svg { width: 66px; height: 66px; }

  .how-panel {
    position: absolute; left: 503px; top: 554px; width: 297px; height: 516px;
    background: var(--purple-panel); border-radius: 22px 0 0 22px;
  }
  .how-title {
    position: absolute; left: 520px; top: 566px;
    font-family: "Roboto Condensed", sans-serif; font-weight: 800; font-size: 36px; color: var(--teal);
  }
  .steps { position: absolute; left: 520px; top: 612px; width: 250px; list-style: none; }
  .steps li { position: relative; padding-left: 24px; font-size: 20px; line-height: 1.3; color: var(--white); margin-bottom: 8px; }
  .steps li svg { position: absolute; left: 0; top: 3px; width: 18px; height: 18px; }

  .offer-blob { position: absolute; left: 530px; top: 862px; width: 195px; height: 180px; border-radius: 48% 52% 46% 54% / 50% 44% 56% 50%; background: var(--teal-soft); }
  .offer { position: absolute; left: 530px; top: 886px; width: 195px; text-align: center; font-family: "Roboto Condensed", sans-serif; color: var(--white); }
  .offer .label { font-size: 22px; font-weight: 400; line-height: 1; }
  .offer .price { font-size: 54px; font-weight: 800; color: var(--yellow); line-height: 1; }
  .offer .code-label { font-size: 22px; line-height: 1.1; }
  .offer .code { display: inline-block; background: var(--yellow); color: var(--ink); font-weight: 800; font-size: 24px; padding: 0 20px; line-height: 1.1; }

  .web {
    position: absolute; left: 0; top: 1087px; width: 800px; text-align: center;
    font-size: 22px; font-weight: 600; color: var(--white);
  }
</style>
</head>
<body>
<main class="flyer">
  <div class="pet-photo" role="img" aria-label="Photo of a ginger kitten sitting beside a cream labrador puppy"></div>

  <header class="brand">
    <span class="brand-mark"></span>
    <div class="brand-name">PAW POST</div>
  </header>

  <svg class="bubble" viewBox="0 0 430 316" aria-hidden="true">
    <defs>
      <linearGradient id="bubbleFill" x1="0" y1="0" x2="1" y2="1">
        <stop offset="0" stop-color="#17b3a3"/>
        <stop offset="1" stop-color="#0f9088"/>
      </linearGradient>
    </defs>
    <path d="M120 40 Q124 2 170 2 L396 2 Q428 2 424 40 L392 274 Q386 312 346 312 L86 312 Q48 312 52 274 L62 170 Q30 146 8 76 Q40 126 66 132 Z" fill="url(#bubbleFill)"/>
  </svg>
  <div class="bubble-text">
    <div class="lead">THE BEST</div>
    <div class="line">PROTECTION</div>
    <div class="line">AND CARE</div>
    <div class="line">FOR YOUR</div>
    <div class="line">PET</div>
    <div class="sign">with PAW POST</div>
  </div>

  <section class="lower"></section>
  <svg class="why-shape" viewBox="0 0 800 584" aria-hidden="true">
    <path d="M0 100 Q150 80 240 130 Q310 190 305 300 Q298 420 200 470 Q110 500 0 496 Z" fill="#ffffff"/>
  </svg>
  <div class="base-strip"></div>

  <h2 class="why-title">WHY PAW<br>POST?</h2>

  <div class="benefits">
    <div class="benefit"><h3>Protection &amp; Care</h3><p>Protection against all major parasites to avoid putting your pet and your family at risk</p></div>
    <div class="benefit"><h3>In Time</h3><p>Never having to remember when to treat your pet</p></div>
    <div class="benefit"><h3>Convenient</h3><p>Delivered directly to your letter box</p></div>
    <div class="benefit"><h3>Low cost</h3><p>All the high end, trusted brands but cheaper than the vet</p></div>
  </div>

  <div class="icon-bubble" style="left:196px;top:558px;">
    <svg viewBox="0 0 64 64" fill="none" stroke="#00a990" stroke-width="3" stroke-linejoin="round"><path d="M32 4 L56 12 V30 Q56 50 32 60 Q8 50 8 30 V12 Z"/><path d="M32 10 L50 16 V30 Q50 46 32 54 Q14 46 14 30 V16 Z"/><circle cx="32" cy="34" r="6"/></svg>
  </div>
  <div class="icon-bubble" style="left:318px;top:647px;">
    <svg viewBox="0 0 64 64" fill="none" stroke="#00a990" stroke-width="4" stroke-linecap="round"><path d="M56 32 A24 24 0 1 1 44 11"/><path d="M32 20 V34 H42"/><path d="M56 8 L42 22 M42 12 V22 H52"/></svg>
  </div>
  <div class="icon-bubble" style="left:339px;top:815px;">
    <svg viewBox="0 0 64 64" fill="#00a990"><rect x="26" y="6" width="22" height="26" rx="2"/><path d="M4 44 H20 Q30 38 40 44 L54 38 Q60 38 56 44 L40 54 H4 Z"/></svg>
  </div>
  <div class="icon-bubble" style="left:257px;top:949px;">
    <svg viewBox="0 0 64 64" fill="none" stroke="#00a990" stroke-width="4" stroke-linecap="round"><path d="M42 16 Q32 10 24 14 Q18 20 24 26 L40 34 Q46 40 40 46 Q32 50 22 44"/><path d="M32 4 V56 M24 50 L32 58 L40 50"/></svg>
  </div>

  <section class="how-panel"></section>
  <h2 class="how-title">HOW IT WORKS</h2>
  <ul class="steps">
    <li><svg viewBox="0 0 20 20"><path d="M2 10 L8 16 L18 3" fill="none" stroke="#00a990" stroke-width="3"/></svg>Select which pet the treatment is for</li>
    <li><svg viewBox="0 0 20 20"><path d="M2 10 L8 16 L18 3" fill="none" stroke="#00a990" stroke-width="3"/></svg>Choose your treatment type</li>
    <li><svg viewBox="0 0 20 20"><path d="M2 10 L8 16 L18 3" fill="none" stroke="#00a990" stroke-width="3"/></svg>Select your preferred brand Choose between 1, 3, 6 or 12 months treatment</li>
  </ul>

  <div class="offer-blob"></div>
  <div class="offer">
    <div class="label">FIRST BOX</div>
    <div class="price">£5.99</div>
    <div class="code-label">USE CODE</div>
    <div class="code">XXX</div>
  </div>

  <div class="web">www.pawpost.co.uk</div>
</main>
</body>
</html>
```